Presentation and Communication Coaching Services Business needs updated interactive web site

I want to keep the color scheme, functionality, and pages of my current site, but with a newer/updated look. I need to improve security and simplify images, etc. (Please see current site http://brackwellvoicetutor.com ) This will need be functional on mobile devices, as well.

I'm attached to the scrolling client list and scrolling client feedback.

Industry/Entity Type

Professional Service

Font styles to use
Sans Serif

Colors
0356a4
f37122
33a6d7

Requirements
Must have
• scrolling client banner on home page, client comments slider, color scheme
• Please see current site: http://brackwellvoicetutor.com
Nice to have
• better action/appearance
Should not have
• I don't want it to look like all the other sites/templates

```html
<!DOCTYPE html>
<html lang="en">
<head>
<meta charset="utf-8">
<title>Brackwell Voice Consulting</title>
<link rel="stylesheet" href="https://fonts.googleapis.com/css2?family=Montserrat:wght@400;500;600;700&display=swap">
<style>
  :root {
    --blue-deep: #0356a4;
    --blue-mid: #1468b4;
    --blue-light: #1f84c4;
    --orange: #f37122;
    --white: #ffffff;
    --ink: #4a4a4a;
    --hero-dark: #2a2326;
    --hero-mid: #4a3b42;
  }
  * { margin: 0; padding: 0; box-sizing: border-box; }
  html, body { width: 1164px; height: 1200px; overflow: hidden; }
  body {
    position: relative;
    font-family: "Montserrat", sans-serif;
    background: var(--white);
    color: var(--ink);
  }
  .top-band {
    position: absolute; left: 0; top: 0; width: 1164px; height: 774px;
    background: linear-gradient(180deg, var(--blue-deep) 0%, var(--blue-mid) 45%, var(--blue-light) 100%);
    box-shadow: 0 2px 4px rgba(0,0,0,0.18);
  }
  .brand {
    position: absolute; left: 58px; top: 6px;
    font-size: 12px; font-weight: 400; color: var(--white); letter-spacing: -0.2px;
  }
  .main-nav {
    position: absolute; top: 8px; left: 0; width: 1164px;
    font-size: 9.5px; font-weight: 600; color: var(--white);
  }
  .main-nav a { position: absolute; color: inherit; text-decoration: none; white-space: nowrap; }
  .main-nav a.is-active { color: var(--orange); padding: 0 7px 4px; border-bottom: 1px solid var(--orange); }
  .login { display: flex; align-items: center; gap: 7px; }
  .hero {
    position: absolute; left: 58px; top: 48px; width: 1049px; height: 333px;
    background:
      radial-gradient(ellipse 260px 150px at 560px 170px, #6a5a62 0%, transparent 70%),
      linear-gradient(90deg, var(--hero-dark) 0%, var(--hero-mid) 50%, var(--hero-dark) 100%);
  }
  .hero-arrow { position: absolute; top: 160px; }
  .hero-arrow.prev { left: 56px; }
  .hero-arrow.next { left: 962px; }
  .hero-caption {
    position: absolute; left: 150px; top: 155px; width: 749px;
    text-align: center; color: var(--white);
    font-size: 12px; font-weight: 500; line-height: 20px;
  }
  .slider-dots { position: absolute; top: 405px; left: 547px; display: flex; gap: 8px; align-items: center; }
  .slider-dots span { height: 6px; border-radius: 3px; background: var(--white); }
  .intro-photo {
    position: absolute; left: 57px; top: 453px; width: 319px; height: 232px;
    background: linear-gradient(120deg, #e9eef0 0%, #c9d2cf 45%, #9aa7a0 70%, #e6ebec 100%);
  }
  .intro-copy { position: absolute; left: 469px; top: 450px; width: 640px; color: var(--white); text-transform: uppercase; }
  .intro-copy h1 { font-size: 15.5px; font-weight: 700; margin-bottom: 5px; letter-spacing: 0.1px; }
  .intro-copy p { font-size: 12.4px; font-weight: 500; line-height: 22.6px; }
  .intro-copy p.closing { font-weight: 700; margin-top: 22px; }
  .pillars { position: absolute; top: 852px; left: 0; width: 1164px; }
  .pillar { position: absolute; width: 230px; text-align: center; text-transform: uppercase; }
  .pillar-icon {
    width: 113px; height: 113px; border-radius: 50%; background: var(--orange);
    margin: 0 auto; display: flex; align-items: center; justify-content: center;
    box-shadow: 0 10px 14px rgba(0,0,0,0.22);
  }
  .pillar h2 { font-size: 16px; font-weight: 400; color: #444; margin-top: 37px; letter-spacing: 0.5px; }
  .pillar p { font-size: 11.5px; font-weight: 400; line-height: 21px; margin-top: 6px; letter-spacing: 0.4px; }
</style>
</head>
<body>
  <div class="top-band"></div>

  <div class="brand">brackwellvoiceconsulting</div>

  <nav class="main-nav">
    <a class="is-active" href="#" style="left:276px">HOME</a>
    <a href="#" style="left:365px">ABOUT</a>
    <a href="#" style="left:452px">CLIENT</a>
    <a href="#" style="left:539px">REVIEWS</a>
    <a href="#" style="left:643px">SERVICES</a>
    <a href="#" style="left:752px">CONTACT</a>
    <a href="#" style="left:861px">SPEAKING SECRETS</a>
    <a href="#" class="login" style="left:1053px;top:-3px">LOGIN
      <svg width="15" height="16" viewBox="0 0 15 16" fill="none" stroke="#fff" stroke-width="1.2">
        <circle cx="7.5" cy="5" r="3.8"/><path d="M1 15.5c0-4 2.8-6 6.5-6s6.5 2 6.5 6z"/>
      </svg>
    </a>
  </nav>

  <section class="hero" role="img" aria-label="Close-up of a stage microphone in front of a blurred audience">
    <svg class="hero-arrow prev" width="31" height="18" viewBox="0 0 31 18" fill="none" stroke="#fff" stroke-width="2.5">
      <path d="M30 9H3M10 1.5L2.5 9 10 16.5"/>
    </svg>
    <p class="hero-caption">Lorem Ipsum is simply dummy text of the printing and typesetting industry. Lorem Ipsum has been the industry's standard dummy text ever since the 1500s, when an unknown printer took a galley of type and scrambled it to make a type specimen book.</p>
    <svg class="hero-arrow next" width="31" height="18" viewBox="0 0 31 18" fill="none" stroke="#fff" stroke-width="2.5">
      <path d="M1 9h27M21 1.5L28.5 9 21 16.5"/>
    </svg>
  </section>

  <div class="slider-dots">
    <span style="width:35px"></span><span style="width:15px"></span><span style="width:7px;height:7px"></span>
  </div>

  <div class="intro-photo" role="img" aria-label="Smiling professional woman in a grey blazer in a bright office"></div>

  <div class="intro-copy">
    <h1>You’re good at what you do. Learn how to let it show.</h1>
    <p>An individual works hard to reach a place of respect and authority in her or his chosen profession. Effective self-presentation adds confidence and allows one’s unique personality and expertise to shine through – in fact, it is key in separating from the pack and reaching higher goals. As competition increases, these skills become more essential in demonstrating value to an employer, manager, or board.</p>
    <p class="closing">You’ve done your best to reach this professional level. It’s time to develop what it takes to reach the next one.</p>
  </div>

  <section class="pillars">
    <div class="pillar" style="left:73px">
      <div class="pillar-icon">
        <svg width="54" height="54" viewBox="0 0 54 54" fill="none" stroke="#fff" stroke-width="3.5">
          <path d="M15 4h24v14c0 9-5 15-12 15S15 27 15 18z" fill="#fff"/>
          <path d="M15 8H6c0 10 5 14 10 14M39 8h9c0 10-5 14-10 14"/>
          <path d="M27 33v9M18 48h18" stroke-width="5"/>
        </svg>
      </div>
      <h2>The Goal</h2>
      <p>Deliver a focused, engaging message that leads to a successful outcome.</p>
    </div>
    <div class="pillar" style="left:334px">
      <div class="pillar-icon">
        <svg width="54" height="60" viewBox="0 0 54 60" fill="#fff">
          <rect x="24" y="4" width="6" height="54"/>
          <path d="M10 12h32l6 4-6 4H10z"/><path d="M44 26H14l-6 4 6 4h30z"/><path d="M12 40h28l5 3-5 3H12z"/>
        </svg>
      </div>
      <h2>The Challenge</h2>
      <p>Find a path to develop skills and strategies to accomplish this aim while also projecting confidence, warmth, and credibility.</p>
    </div>
    <div class="pillar" style="left:595px">
      <div class="pillar-icon">
        <svg width="62" height="62" viewBox="0 0 62 62" fill="none" stroke="#fff">
          <circle cx="31" cy="31" r="22" stroke-width="7" stroke-dasharray="4.3 4.3"/>
          <circle cx="31" cy="31" r="17" stroke-width="5"/>
        </svg>
      </div>
      <h2>The Solution</h2>
      <p>Obtain individualized coaching to grow these necessary skills and establish a reliable strategy to hit the mark every time.</p>
    </div>
    <div class="pillar" style="left:857px">
      <div class="pillar-icon">
        <svg width="60" height="60" viewBox="0 0 60 60" fill="none" stroke="#fff" stroke-width="2.5" stroke-linejoin="round">
          <path d="M4 56l18-14-4-6 18-14 6-6M38 8h10v10"/>
        </svg>
      </div>
      <h2>The Result</h2>
      <p>A natural, confident delivery that comes from knowing what you’re doing, how to reach your goal.</p>
    </div>
  </section>
</body>
</html>
```